BrightLoom Sound Screen website

I need a website that looks clean and I have the ability to update on my own with pics and text. Want it to be a very easy to use and interesting site. With designs please give me a desription. Want the feel to be for everyone. My goal with my business is so that everyone can enjoy the modern technology that is around us. Please view my temp site for an idea of pics and text. www.brightloomss.example. I am not happy with this site this is why I am asking for much needed help.
Updates

Reason: Havent had a chance to site down and view all submissions.

Target Market(s)

Clients/business with some expendable income.

Requirements
Must have
• Want a Home, Services, About Us, Contact Us, Products, Phone Support, and Local Support pages. Must have the ability for me to go in and update pages with text and images. First page will have a sales and a current project sections. Hosting is done on Godaddy and I need to know how to transfer once site is complete.

```html
<!DOCTYPE html>
<html lang="en">
<head>
<meta charset="utf-8">
<title>BrightLoom Sound Screen</title>
<link rel="stylesheet" href="https://fonts.googleapis.com/css2?family=Source+Sans+3:ital,wght@0,300;0,400;0,600;1,400&display=swap">
<style>
:root{
  --blue-deep:#0f3f6c;
  --blue-nav:#164d80;
  --blue-mid:#2f73ad;
  --blue-head:#1f5b8e;
  --blue-link:#2a74b3;
  --text:#7a7a7a;
  --text-dark:#555;
  --panel:#f3f3f3;
  --line:#d8d8d8;
  --white:#fff;
}
*{margin:0;padding:0;box-sizing:border-box}
html,body{width:849px;height:1200px;overflow:hidden}
body{font-family:"Source Sans 3",sans-serif;background:var(--white);color:var(--text);position:relative;font-size:10px;line-height:15px}
.abs{position:absolute}
.topstrip{left:0;top:0;width:849px;height:12px;background:#e9e9e9}
.header{left:0;top:12px;width:849px;height:113px;background:linear-gradient(#fff,#f1f1f1)}
.brand{left:37px;top:60px;display:flex;align-items:center;gap:8px;font-size:25px;font-weight:600;color:var(--blue-head);line-height:25px}
.brand-dot{width:14px;height:14px;border-radius:50%;background:var(--blue-mid)}
.search{left:635px;top:43px;width:183px;height:22px;border:1px solid #d6d6d6;border-radius:4px;background:#fff;font-size:9px;color:#aaa;padding:3px 8px;box-shadow:0 2px 3px rgba(0,0,0,.08)}
.search svg{position:absolute;right:6px;top:4px}
.nav{left:245px;top:86px;width:595px;height:39px;background:linear-gradient(var(--blue-nav),var(--blue-deep));border-radius:4px 4px 0 0;display:flex}
.nav a{color:#dbe7f3;text-decoration:none;font-size:12.5px;line-height:39px;padding:0 11px;border-right:1px solid rgba(255,255,255,.12)}
.nav a:first-child{background:#0c3458;padding:0 25px;border-radius:4px 0 0 0}
.nav a:nth-child(2){padding:0 17px}
.nav a:last-child{border-right:none}
.banner{left:0;top:125px;width:849px;height:317px;background:radial-gradient(ellipse at 60% 30%,#3c84bf,#1d5d96 55%,#124579)}
.hero-photo{left:30px;top:155px;width:456px;height:252px;border:4px solid #fff;background:linear-gradient(135deg,#b98a55,#7c5432 60%,#4a2f1d);box-shadow:0 4px 8px rgba(0,0,0,.35)}
.hero-title{left:514px;top:174px;font-size:24px;font-weight:400;color:#fff;line-height:30px;border-bottom:1px solid rgba(255,255,255,.5);padding-right:6px}
.hero-sub{left:514px;top:204px;font-size:18px;font-weight:300;color:#cfe0f0;line-height:24px}
.hero-text{left:514px;top:236px;width:290px;font-size:9.5px;line-height:15px;color:#e2ecf6}
.hero-text p{margin-bottom:4px}
.btn{left:520px;top:328px;width:82px;height:24px;background:#123d66;border-radius:3px;color:#d8e6f3;font-size:10px;line-height:24px;text-align:center}
.dots{left:524px;top:388px;display:flex;gap:4px}
.dots i{width:8px;height:8px;border-radius:50%;background:#fff;display:block}
h2{font-weight:400;font-size:15px;color:var(--blue-head);line-height:20px}
.welcome{left:19px;top:468px;width:550px}
.welcome h2{margin-bottom:3px}
.welcome p{font-size:9.5px;line-height:15px;margin-bottom:3px}
.welcome p.gap{margin-top:20px}
.featured{left:19px;top:716px;width:550px}
.service{position:absolute;left:-2px;width:552px;height:90px}
.service .ph{position:absolute;left:0;top:0;width:150px;height:88px;background:linear-gradient(135deg,#e8e4df,#a9a39d)}
.service h3{position:absolute;left:160px;top:0;font-size:11px;font-weight:400;color:var(--blue-link)}
.service p{position:absolute;left:160px;top:17px;width:395px;font-size:9.5px;line-height:15px;color:var(--blue-link)}
.side{left:585px;width:245px;background:var(--panel)}
.side-head{height:31px;border:1px solid var(--line);background:linear-gradient(#fff,#eee);border-radius:4px 4px 0 0;font-size:14px;color:var(--blue-head);line-height:30px;padding-left:12px}
.post{position:absolute;left:7px;width:236px}
.post .th{position:absolute;left:0;top:0;width:64px;height:58px;background:linear-gradient(#6b6b6b,#2d2d2d)}
.post .date{position:absolute;left:72px;top:-3px;font-size:11.5px;color:#555}
.post p{position:absolute;left:72px;top:13px;width:160px;font-size:9px;line-height:13.5px;font-style:italic;color:#888}
.tabs{display:flex;height:31px;border:1px solid var(--line);border-radius:4px 4px 0 0;background:linear-gradient(#fff,#eee)}
.tabs span{font-size:14px;line-height:30px;color:var(--blue-head);padding:0 10px}
.tabs .on{background:#e6e9ee;border-right:1px solid var(--line)}
.proj .th{left:10px;width:80px;height:68px;background:linear-gradient(135deg,#d6e4ef,#8aa6bd);border:3px solid #ddd}
.proj .date{left:105px}
.proj p{left:105px;width:128px}
.footer{left:0;top:983px;width:849px;height:217px;background:#f2f2f2}
.fcol{position:absolute;top:0;height:162px;border-right:1px dotted #bbb}
.fcol h4{font-weight:400;font-size:13px;color:#555;margin-top:22px;margin-bottom:12px}
.fcol li{list-style:none;font-size:9.5px;line-height:19px;color:#888}
.social{display:flex;gap:4px;margin-bottom:10px}
.social i{display:block;width:18px;height:18px;border-radius:3px;background:var(--blue-mid)}
.flinks{font-size:9.5px;color:#888}
.frule{left:30px;top:1146px;width:792px;height:1px;background:#d6d6d6}
.copy{left:22px;top:1160px;font-size:9.5px;color:#777}
</style>
</head>
<body>
<div class="abs topstrip"></div>
<header class="abs header"></header>
<div class="abs brand"><span class="brand-dot"></span>BrightLoom</div>
<div class="abs search">type your word here
  <svg width="14" height="14" viewBox="0 0 14 14"><circle cx="5.5" cy="5.5" r="4" fill="none" stroke="#bbb" stroke-width="1.6"/><line x1="8.5" y1="8.5" x2="13" y2="13" stroke="#bbb" stroke-width="2"/></svg>
</div>
<nav class="abs nav">
  <a>Home</a><a>About Us</a><a>Services</a><a>Gallery</a><a>Contact Us</a><a>Packaged Solutions</a><a>Help Us Support</a>
</nav>

<section class="abs banner"></section>
<div class="abs hero-photo" role="img" aria-label="Photo of a conference room with a wall video display"></div>
<h1 class="abs hero-title">BrightLoom Sound Screen</h1>
<div class="abs hero-sub">Punch line Goes here</div>
<div class="abs hero-text">
  <p>Lumenfield Studio is a web service company, offering a wide range of services which range from designing and development, that is covering almost all the fields in the best possible way.</p>
  <p>To be the best we know what and how to present beautifully the working of the client's need and their advantages be highlighted.</p>
</div>
<div class="abs btn">READ MORE ›</div>
<div class="abs dots"><i></i><i></i><i></i><i></i></div>

<section class="abs welcome">
  <h2>Welcome to Our Website Mainpage</h2>
  <p>Lumenfield Studio is a web service company, offering a wide range of services which range from designing and development, that is covering almost all the fields in the best possible way. To be the best we know what and how to present beautifully the working of the client's need and their advantages be highlighted. We act in accordance with the Industry certified processes to deliver the best to our clients all over the world. Over years we have built a strong reputation in providing website design and web development services.</p>
  <p class="gap">Thus, Wanna get ahead in the competition with other websites.... Lumenfield Studio provide you with an attractive and most convincing website to enhance your marketing goals.</p>
  <p>The only way to success is through the right path and that's what we provide you. None of the other companies has the result we do. So stick to the best that's how you will be the best don't opt for the second best. Our expertise does not limit itself to web development but also it includes Web Hosting, Search Engine Optimization, E-Commerce. We partner hundreds of organization to enhance their business, marketing and profit goals.</p>
</section>

<section class="abs featured">
  <h2>Featured Services Overview</h2>
  <div class="service" style="top:32px">
    <div class="ph" role="img" aria-label="Photo of a team working at a laptop"></div>
    <h3>YOUR TITILE GOES HERE</h3>
    <p>Lumenfield Studio is a web service company, offering a wide range of services which range from designing and development, that is covering almost all the fields in the best possible way. To be the best we know what and how to present beautifully the working of the client's need and their advantages be highlighted.</p>
  </div>
  <div class="service" style="top:136px">
    <div class="ph" role="img" aria-label="Photo of two colleagues at a computer"></div>
    <h3>YOUR TITILE GOES HERE</h3>
    <p>Lumenfield Studio is a web service company, offering a wide range of services which range from designing and development, that is covering almost all the fields in the best possible way. To be the best we know what and how to present beautifully the working of the client's need and their advantages be highlighted.</p>
  </div>
</section>

<aside class="abs side" style="top:461px;height:262px">
  <div class="side-head">Recent Blog &amp; News</div>
  <div class="post" style="top:44px"><div class="th" role="img" aria-label="Photo of a projection screen room"></div><div class="date">20.March.2012</div><p>Lumenfield Studio is a professional website design company dedicated to provide excellent services.</p></div>
  <div class="post" style="top:115px"><div class="th" role="img" aria-label="Photo of a projector lens"></div><div class="date">20.March.2012</div><p>Lumenfield Studio is a professional website design company dedicated to provide excellent services.</p></div>
  <div class="post" style="top:185px"><div class="th" role="img" aria-label="Photo of a touch control panel"></div><div class="date">20.March.2012</div><p>Lumenfield Studio is a professional website design company dedicated to provide excellent services.</p></div>
</aside>

<aside class="abs side proj" style="top:729px;height:245px">
  <div class="tabs"><span class="on">Current Project</span><span style="padding-left:22px">Sale</span></div>
  <svg class="abs" style="left:222px;top:36px" width="14" height="9" viewBox="0 0 14 9"><path d="M6 0L0 4.5 6 9z M8 0l6 4.5L8 9z" fill="#b5b5b5"/></svg>
  <div class="post" style="top:44px;left:0"><div class="th abs" role="img" aria-label="Photo of a calculator and pen on a chart"></div><div class="date abs">20.March.2012</div><p class="abs">Lumenfield Studio is a professional website design company dedicated to provide excellent services.</p></div>
  <div class="post" style="top:128px;left:0"><div class="th abs" role="img" aria-label="Photo of a calculator and pen on a chart"></div><div class="date abs">20.March.2012</div><p class="abs">Lumenfield Studio is a professional website design company dedicated to provide excellent services.</p></div>
</aside>

<footer class="abs footer">
  <div class="fcol" style="left:31px;width:124px"><h4>Our Company</h4><ul><li>Main Page</li><li>About Our Company</li><li>Recent Blog &amp; Comments</li></ul></div>
  <div class="fcol" style="left:181px;width:106px"><h4>About Us</h4><ul><li>Why We Are</li><li>What We Do</li><li>Support &amp; Services</li></ul></div>
  <div class="fcol" style="left:306px;width:131px"><h4>Services Overview</h4><ul><li>Our First Services</li><li>Second Services</li><li>Third Services here</li><li>Our Fouth Services</li></ul></div>
  <div class="fcol" style="left:469px;width:200px;border:none">
    <h4>Get In Touch</h4>
    <div class="social"><i></i><i></i><i></i><i></i></div>
    <div class="flinks">Pagefeed &nbsp;|&nbsp; Worknet &nbsp;|&nbsp; Chirper &nbsp;|&nbsp; Searchly</div>
  </div>
</footer>
<div class="abs frule"></div>
<div class="abs copy">copyright © 2012 Company Name &nbsp;|&nbsp; All right reserved</div>
</body>
</html>
```